Solace Chiropractic & Acupuncture Business Cards

I need a business card design that feels elevated. I am open to any of the logo designs uploaded. We have two doctors so I'll need to be able to change out the names.

Information:
Marnie Toller D.C., Dipl. Ac. ASA
584 W 12th St, Ste 320
Hutchinson, KS 67419
solacegrove.net
620-555-0147
drmarnie@solacegrove.com
Updates

We have designs we like now, we are just trying to choose between top contenders. Thanks for your submissions!

Contact Information for Business Card

noted in description

Requirements
Must have
• ability to edit info if possible
Nice to have
• Please see our website solacegrove.net for our style and colors

```html
<!DOCTYPE html>
<html lang="en">
<head>
<meta charset="UTF-8">
<title>Solace Chiropractic &amp; Acupuncture — Business Cards</title>
<link rel="stylesheet" href="https://fonts.googleapis.com/css2?family=Poppins:wght@300;400;700&display=swap">
<style>
  :root {
    --page-bg: #e9e1dc;
    --card-bg: #f4f2ee;
    --card-edge: #e4e0d8;
    --navy: #343b52;
    --ink: #1f2330;
    --sleeve: #39496b;
    --peach: #f1d5c2;
  }
  * { box-sizing: border-box; margin: 0; padding: 0; }
  html, body {
    width: 1200px; height: 1109px; overflow: hidden;
    background: var(--page-bg);
    font-family: "Poppins", sans-serif;
  }
  .stage {
    width: 1200px; height: 1109px;
    display: flex; flex-direction: column; align-items: center; justify-content: center;
    gap: 70px;
  }
  .card {
    width: 700px; height: 400px; position: relative;
    box-shadow: 0 8px 18px rgba(60, 45, 35, 0.22);
  }
  .card-front {
    background: radial-gradient(ellipse at 55% 45%, #ffffff 0%, var(--card-bg) 55%, var(--card-edge) 100%);
    color: var(--ink);
  }
  .brand {
    position: absolute; left: 40px; top: 120px; width: 205px;
    display: flex; align-items: flex-start; gap: 12px;
    color: var(--navy);
    font-weight: 400; font-size: 21px; line-height: 1.3; text-transform: uppercase; letter-spacing: 0.5px;
  }
  .brand-mark {
    flex: none; width: 14px; height: 14px; margin-top: 8px;
    border-radius: 50%; background: var(--navy);
  }
  .divider {
    position: absolute; left: 275px; top: 100px; width: 2px; height: 210px;
    background: var(--navy);
  }
  .details { position: absolute; left: 310px; top: 62px; }
  .doctor-name { font-weight: 700; font-size: 31px; color: var(--navy); line-height: 1.2; }
  .credentials { font-weight: 400; font-size: 20px; line-height: 1.35; margin-top: 4px; }
  .address { font-size: 24px; line-height: 1.3; margin-top: 22px; }
  .contacts { list-style: none; margin-top: 14px; font-size: 24px; line-height: 1.25; }
  .contacts li { display: flex; align-items: center; gap: 10px; }
  .contacts svg { width: 20px; height: 20px; flex: none; fill: none; stroke: var(--navy); stroke-width: 2; }
  .card-back {
    background: var(--sleeve);
    display: flex; align-items: center; justify-content: center;
  }
  .back-name {
    color: var(--peach); font-weight: 300; font-size: 40px; letter-spacing: 1px;
  }
</style>
</head>
<body>
<main class="stage">
  <section class="card card-front" aria-label="Business card front">
    <div class="brand">
      <span class="brand-mark"></span>
      <span class="brand-name">Solace Chiropractic &amp; Acupuncture</span>
    </div>
    <div class="divider"></div>
    <div class="details">
      <h1 class="doctor-name">Marnie Toller</h1>
      <p class="credentials">Doctor of Chiropractic<br>Dipl. Ac. ASA</p>
      <p class="address">584 W 12th St, Ste 320<br>Hutchinson, KS 67419</p>
      <ul class="contacts">
        <li>
          <svg viewBox="0 0 24 24" aria-hidden="true"><path d="M5 3h4l2 5-3 2a12 12 0 0 0 6 6l2-3 5 2v4a2 2 0 0 1-2 2A17 17 0 0 1 3 5a2 2 0 0 1 2-2z"/></svg>
          620-555-0147
        </li>
        <li>
          <svg viewBox="0 0 24 24" aria-hidden="true"><circle cx="12" cy="12" r="9"/><path d="M3 12h18M12 3c3 3 3 15 0 18M12 3c-3 3-3 15 0 18"/></svg>
          solacegrove.net
        </li>
        <li>
          <svg viewBox="0 0 24 24" aria-hidden="true"><path d="M21 3L3 11l7 3 3 7z" fill="#343b52"/></svg>
          drmarnie@solacegrove.com
        </li>
      </ul>
    </div>
  </section>

  <section class="card card-back" aria-label="Business card back">
    <p class="back-name">Solace Chiropractic</p>
  </section>
</main>
</body>
</html>
```